Business Cards and Stationery for Borvexa engineering company.
Borvexa
Business Cards and Stationery for Borvexa engineering company. - Engineering
Creative Brief
Simple
Delgado Tarvin
Veltmark Region, Harlow-on-Tessen, st. Korvell, 283/7 office 42
tarvindelgado@mailbrook.example
logo on different backgrounds

```html
<!DOCTYPE html>
<html lang="en">
<head>
<meta charset="utf-8">
<title>Borvexa – Business Cards</title>
<link href="https://fonts.googleapis.com/css2?family=Open+Sans:wght@400;600;700&display=swap" rel="stylesheet">
<style>
  :root {
    --bg: #d6cfc7;
    --brand-blue: #1d6fd1;
    --band-top: #4ea3ec;
    --band-mid: #1a73d6;
    --band-deep: #0c4fa8;
    --silver-light: #f4f5f7;
    --silver-dark: #a9adb3;
    --card-white: #ffffff;
    --card-grey: #e9ebee;
    --ink: #1e2a3a;
    --glass: rgba(236, 240, 244, 0.78);
    --glass-edge: rgba(255, 255, 255, 0.9);
    --white: #ffffff;
  }
  * { margin: 0; padding: 0; box-sizing: border-box; }
  html, body { width: 1200px; height: 730px; overflow: hidden; }
  body {
    background: var(--bg);
    font-family: "Open Sans", Arial, sans-serif;
    position: relative;
  }
  .card {
    position: absolute;
    width: 480px;
    height: 320px;
    border-radius: 22px;
    overflow: hidden;
    background: linear-gradient(180deg, var(--card-white) 0%, var(--card-grey) 100%);
    box-shadow: 0 8px 22px rgba(40, 40, 40, 0.28);
  }
  .card--glass {
    background: linear-gradient(180deg, var(--glass) 0%, rgba(220, 226, 232, 0.7) 100%);
    border: 1px solid var(--glass-edge);
  }
  .card--front.card--solid { left: 72px; top: 40px; }
  .card--front.card--glass { left: 648px; top: 40px; }
  .card--back.card--solid { left: 72px; top: 390px; }
  .card--back.card--glass { left: 648px; top: 390px; }

  .logo {
    position: absolute;
    top: 44px;
    left: 0; right: 0;
    display: flex;
    justify-content: center;
    align-items: center;
    gap: 12px;
  }
  .logo__mark {
    width: 54px; height: 54px;
    border-radius: 50%;
    background: var(--brand-blue);
  }
  .logo__name {
    font-weight: 700;
    font-size: 40px;
    color: var(--brand-blue);
    letter-spacing: 0.5px;
  }
  .logo--mirrored { transform: scaleX(-1); opacity: 0.55; }

  .holder {
    position: absolute;
    top: 186px; left: 0; right: 0;
    text-align: center;
    font-weight: 700;
    font-size: 16px;
    color: var(--ink);
  }
  .silver-line {
    position: absolute;
    left: 0; right: 0;
    height: 6px;
    background: linear-gradient(180deg, var(--silver-light), var(--silver-dark));
  }
  .band {
    position: absolute;
    left: 0; right: 0; bottom: 0;
    background: linear-gradient(180deg, var(--band-top) 0%, var(--band-mid) 45%, var(--band-deep) 100%);
  }
  .card--front .silver-line { top: 212px; }
  .card--front .band { top: 218px; }
  .card--back .silver-line { top: 168px; }
  .card--back .band { top: 174px; }

  .contacts {
    position: absolute;
    left: 0; right: 0; top: 26px;
    color: var(--white);
    font-size: 10px;
    display: flex;
    flex-direction: column;
    align-items: center;
    gap: 6px;
  }
  .contacts__row { display: flex; gap: 14px; align-items: center; }
  .contact { display: flex; align-items: center; gap: 5px; white-space: nowrap; }
  .contact svg { width: 12px; height: 12px; flex: none; }

  .web {
    position: absolute;
    left: 0; right: 0; top: 64px;
    text-align: center;
    color: var(--white);
    font-size: 14px;
    font-weight: 600;
    letter-spacing: 5px;
  }
</style>
</head>
<body>

  <section class="card card--front card--solid">
    <div class="logo"><span class="logo__mark"></span><span class="logo__name">Borvexa</span></div>
    <p class="holder">Delgado Tarvin</p>
    <div class="silver-line"></div>
    <div class="band">
      <div class="contacts">
        <div class="contacts__row">
          <span class="contact">
            <svg viewBox="0 0 14 14"><circle cx="7" cy="7" r="7" fill="#fff"/><path d="M7 3.2a2.4 2.4 0 0 0-2.4 2.4c0 1.8 2.4 4.8 2.4 4.8s2.4-3 2.4-4.8A2.4 2.4 0 0 0 7 3.2z" fill="#1a73d6"/></svg>
            Veltmark Region, Harlow-on-Tessen, st. Korvell, 283/7 office 42
          </span>
          <span class="contact">
            <svg viewBox="0 0 14 14"><circle cx="7" cy="7" r="7" fill="#fff"/><path d="M4.6 3.6l1.3-.3.8 1.8-.8.7a5 5 0 0 0 2.3 2.3l.7-.8 1.8.8-.3 1.3c-3.3.2-6-2.5-5.8-5.8z" fill="#1a73d6"/></svg>
            46203317580
          </span>
        </div>
        <div class="contacts__row">
          <span class="contact">
            <svg viewBox="0 0 14 14"><circle cx="7" cy="7" r="7" fill="#fff"/><rect x="3.5" y="4.5" width="7" height="5" fill="none" stroke="#1a73d6" stroke-width="1"/><path d="M3.5 4.5L7 7.3l3.5-2.8" fill="none" stroke="#1a73d6" stroke-width="1"/></svg>
            tarvindelgado@mailbrook.example
          </span>
          <span class="contact">
            <svg viewBox="0 0 14 14"><circle cx="7" cy="7" r="7" fill="#fff"/><circle cx="7" cy="7" r="3.6" fill="none" stroke="#1a73d6" stroke-width="1"/><path d="M3.4 7h7.2M7 3.4v7.2" stroke="#1a73d6" stroke-width="0.8"/></svg>
            www.borvexa.example
          </span>
        </div>
      </div>
    </div>
  </section>

  <section class="card card--front card--glass">
    <div class="logo"><span class="logo__mark"></span><span class="logo__name">Borvexa</span></div>
    <p class="holder">Delgado Tarvin</p>
    <div class="silver-line"></div>
    <div class="band">
      <div class="contacts">
        <div class="contacts__row">
          <span class="contact">
            <svg viewBox="0 0 14 14"><circle cx="7" cy="7" r="7" fill="#fff"/><path d="M7 3.2a2.4 2.4 0 0 0-2.4 2.4c0 1.8 2.4 4.8 2.4 4.8s2.4-3 2.4-4.8A2.4 2.4 0 0 0 7 3.2z" fill="#1a73d6"/></svg>
            Veltmark Region, Harlow-on-Tessen, st. Korvell, 283/7 office 42
          </span>
          <span class="contact">
            <svg viewBox="0 0 14 14"><circle cx="7" cy="7" r="7" fill="#fff"/><path d="M4.6 3.6l1.3-.3.8 1.8-.8.7a5 5 0 0 0 2.3 2.3l.7-.8 1.8.8-.3 1.3c-3.3.2-6-2.5-5.8-5.8z" fill="#1a73d6"/></svg>
            46203317580
          </span>
        </div>
        <div class="contacts__row">
          <span class="contact">
            <svg viewBox="0 0 14 14"><circle cx="7" cy="7" r="7" fill="#fff"/><rect x="3.5" y="4.5" width="7" height="5" fill="none" stroke="#1a73d6" stroke-width="1"/><path d="M3.5 4.5L7 7.3l3.5-2.8" fill="none" stroke="#1a73d6" stroke-width="1"/></svg>
            tarvindelgado@mailbrook.example
          </span>
          <span class="contact">
            <svg viewBox="0 0 14 14"><circle cx="7" cy="7" r="7" fill="#fff"/><circle cx="7" cy="7" r="3.6" fill="none" stroke="#1a73d6" stroke-width="1"/><path d="M3.4 7h7.2M7 3.4v7.2" stroke="#1a73d6" stroke-width="0.8"/></svg>
            www.borvexa.example
          </span>
        </div>
      </div>
    </div>
  </section>

  <section class="card card--back card--solid">
    <div class="logo"><span class="logo__mark"></span><span class="logo__name">Borvexa</span></div>
    <div class="silver-line"></div>
    <div class="band">
      <p class="web">www.borvexadomain.example</p>
    </div>
  </section>

  <section class="card card--back card--glass">
    <div class="logo logo--mirrored"><span class="logo__mark"></span><span class="logo__name">Borvexa</span></div>
    <div class="silver-line"></div>
    <div class="band">
      <p class="web">www.borvexadomain.example</p>
    </div>
  </section>

</body>
</html>
```